Pet product line, needs a label design

We are a pharmaceutical company focused on animal health. We have been in the Mexican and Central American market for 10 years. During this time we have developed our line for production animals (beef, poultry, dairy, pigs...) and now we want to develop a line for pets.
Our first product are some pills made of Yucca (Yucca schidigera) which helps the digestive system of cats and dogs improve, reducing gas production and diminishing the bad smell of the pet feces.
We are looking for a design that can represent our new product line using this new product as an example, its name is 'BRONTAVEX'. The brand umbrella is TQ Vira, I am attaching this logo.
We need an attractive and original design with a strong personality, capable of jumping to the eyes of the consumer (pet owner) and also attractive for the Veterinarian who will recommend the product.
We want to highlight the benefits of the product by developing icons to the three main claims of the product.
We hope you will find this project attractive and challenging!!

Target Market(s)

Pet owners (mainly dog and cat)

Veterinarians

Industry/Entity Type

Pharmaceutical

Requirements
Must have
• * Product name (BRONTAVEX)
* Label Information (added in a word document)
* Band umbrella logo TQ Vira
* GREAT DESIGN
* The design should be horizontal (5cm height and 13 cm width)
Nice to have
• Nice product name design

Icon designs for the following claims (in spanish):
+ Limpia el trato digestivo (Cleans the digestive tract)
+ Reduce los malos olores (Reduces odors)
+ Propicia la digestión completa (Promotes complete digestion)

```html
<!DOCTYPE html>
<html lang="es">
<head>
<meta charset="utf-8">
<title>Brontavex – Etiqueta</title>
<link rel="stylesheet" href="https://fonts.googleapis.com/css2?family=PT+Sans+Narrow:wght@400;700&family=Kaushan+Script&display=swap">
<style>
  :root {
    --frame: #1bb5ce;
    --panel: #e4f3fb;
    --center-light: #eefafd;
    --center-mid: #8ed9e8;
    --center-deep: #3bbdd6;
    --navy: #1d4f9a;
    --ink: #1b1b1b;
    --ribbon: #1f9bb0;
    --ribbon-dark: #157a8c;
    --green: #8cc63f;
    --white: #ffffff;
    --icon: #3a3a3a;
  }
  * { box-sizing: border-box; margin: 0; padding: 0; }
  html, body { width: 1200px; height: 488px; overflow: hidden; background: var(--frame); }
  body { font-family: "PT Sans Narrow", "Arial Narrow", sans-serif; color: var(--ink); }

  .label { position: relative; width: 1200px; height: 488px; background: var(--frame); }

  .panel-info {
    position: absolute; left: 44px; top: 14px; width: 322px; height: 456px;
    background: var(--panel); padding: 16px 22px;
  }
  .panel-info h3 { font-size: 17px; font-weight: 700; line-height: 1.2; }
  .panel-info p, .panel-info li { font-size: 16px; line-height: 1.3; }
  .ingredients { margin-bottom: 10px; }
  .benefits-intro { margin-bottom: 12px; max-width: 268px; }
  .benefits { list-style: none; }
  .benefits li::before { content: "•"; }
  .disposal-icon { position: absolute; left: 158px; top: 418px; }

  .panel-front {
    position: absolute; left: 366px; top: 14px; width: 467px; height: 456px; overflow: hidden;
    background:
      radial-gradient(circle at 220px 225px, var(--center-light) 0, var(--center-mid) 190px, var(--center-deep) 340px);
  }
  .brand-umbrella {
    position: absolute; left: 132px; top: 44px;
    font-size: 26px; font-weight: 700; color: var(--navy); letter-spacing: .5px;
  }
  .product-name {
    position: absolute; left: 0; top: 52px; width: 467px; text-align: center;
    font-family: "Kaushan Script", cursive; font-size: 98px; line-height: 1;
    color: var(--white); text-shadow: 0 3px 6px rgba(0,60,90,.35);
  }
  .pet-art {
    position: absolute; left: 150px; top: 190px; width: 165px; height: 100px;
    background: linear-gradient(180deg, #bfe9f2, #e9f8fb); border-radius: 8px;
  }
  .ribbon { position: absolute; left: 125px; top: 262px; }
  .pill-art {
    position: absolute; left: 192px; top: 338px; width: 110px; height: 62px;
    background: radial-gradient(ellipse at 60% 45%, #ffffff, #d7e3e8); border-radius: 40px;
  }
  .net-weight {
    position: absolute; left: 24px; top: 437px; font-size: 16px; color: var(--white);
  }
  .count { position: absolute; left: 352px; top: 418px; display: flex; align-items: flex-end; }
  .count-number { font-size: 36px; font-weight: 700; color: var(--navy); line-height: 1; margin-right: 4px; }
  .count-words { display: flex; flex-direction: column; font-size: 14px; line-height: 1; }
  .count-words .top { background: var(--green); color: var(--white); padding: 1px 4px; }
  .count-words .bottom { background: var(--white); color: var(--navy); padding: 1px 4px; }

  .panel-analysis {
    position: absolute; left: 833px; top: 14px; width: 324px; height: 456px;
    background: var(--panel); padding: 17px 22px 0 32px;
  }
  .analysis-table { width: 271px; border-collapse: collapse; background: var(--white); }
  .analysis-table th {
    font-size: 23px; font-weight: 700; text-align: left; padding: 5px 10px; border: 1px solid #333;
  }
  .analysis-table td { font-size: 16px; padding: 2px 8px; border: 1px solid #333; height: 26px; }
  .analysis-table td.value { padding-left: 18px; }
  .analysis-note { font-size: 14px; line-height: 1.45; margin-top: 8px; }
  .analysis-note b { font-weight: 700; }
  .made-by { font-size: 17px; margin-top: 10px; }
  .maker-box {
    margin-top: 8px; width: 104px; height: 78px; background: var(--white);
    display: flex; align-items: center; justify-content: center; gap: 6px;
    font-size: 18px; font-weight: 700; color: var(--navy);
  }
  .maker-box .mark { width: 12px; height: 12px; background: var(--green); }
</style>
</head>
<body>
<main class="label">
  <section class="panel-info">
    <h3>Ingredientes Activos</h3>
    <p class="ingredients">•Saponinas &nbsp;• Glicocomponentes</p>
    <h3>Efectos benéficos en mascotas</h3>
    <p class="benefits-intro">Reduce significativamente los malos olores en los desechos de las mascotas</p>
    <ul class="benefits">
      <li>Reduce el estrés</li>
      <li>Limpia el tracto digestivo</li>
      <li>Propicia una digestión completa</li>
      <li>Efectos anti-inflamatorios</li>
      <li>Efectos antireumáticos</li>
    </ul>
    <svg class="disposal-icon" width="16" height="26" viewBox="0 0 16 26" role="img" aria-label="Depositar en el bote de basura">
      <rect x="1" y="6" width="14" height="2" fill="var(--icon)"/>
      <rect x="6" y="3" width="4" height="3" fill="var(--icon)"/>
      <path d="M2.5 9 H13.5 L12 25 H4 Z" fill="none" stroke="var(--icon)" stroke-width="1.6"/>
      <line x1="6" y1="12" x2="6.5" y2="22" stroke="var(--icon)" stroke-width="1.2"/>
      <line x1="10" y1="12" x2="9.5" y2="22" stroke="var(--icon)" stroke-width="1.2"/>
    </svg>
  </section>

  <section class="panel-front">
    <div class="brand-umbrella">TQ Vira</div>
    <h1 class="product-name">brontavex</h1>
    <div class="pet-art" role="img" aria-label="Silueta de perro y gato"></div>
    <svg class="ribbon" width="215" height="70" viewBox="0 0 215 70" aria-label="Animal Pills">
      <path d="M0 20 L30 18 L30 52 L0 54 L12 37 Z" fill="var(--ribbon-dark)"/>
      <path d="M215 20 L185 18 L185 52 L215 54 L203 37 Z" fill="var(--ribbon-dark)"/>
      <path d="M22 10 Q107 30 193 10 L193 46 Q107 66 22 46 Z" fill="var(--ribbon)"/>
      <text x="107" y="43" text-anchor="middle" font-family="PT Sans Narrow, sans-serif" font-weight="700" font-size="19" fill="#fff">ANIMAL PILLS</text>
    </svg>
    <div class="pill-art" role="img" aria-label="Dos tabletas blancas"></div>
    <p class="net-weight">Net Weight: 000g</p>
    <div class="count">
      <span class="count-number">60</span>
      <span class="count-words"><span class="top">Contenido</span><span class="bottom">Tabletas</span></span>
    </div>
  </section>

  <section class="panel-analysis">
    <table class="analysis-table">
      <thead><tr><th colspan="2">Análisis bromatológico</th></tr></thead>
      <tbody>
        <tr><td>Humedad</td><td class="value">Max. &nbsp;8.2 %</td></tr>
        <tr><td>Proteína Cruda</td><td class="value">Max. &nbsp;2.0 %</td></tr>
        <tr><td>Grasa Cruda</td><td class="value">Max. &nbsp;0.5 %</td></tr>
        <tr><td>Fibra Cruda</td><td class="value">Max. 30.0 %</td></tr>
        <tr><td>Cenizas</td><td class="value">Max. 11.0 %</td></tr>
        <tr><td>Carbohidratos</td><td class="value">Max. 42.5 %</td></tr>
        <tr><td colspan="2">Exchipiente c.b.p.</td></tr>
      </tbody>
    </table>
    <p class="analysis-note"><b>Contenido</b>: Yucca schidigera extracto pulverizado<br><b>Apariencia</b> : Tabletas color café</p>
    <p class="made-by">Manufactured by:</p>
    <div class="maker-box"><span class="mark"></span>TQ Vira</div>
  </section>
</main>
</body>
</html>
```